Business Card for Freelance Copywriting & Web Design Business

Hi! I have a logo but want a new business card. Here's a better idea of what I'm thinking:
-Brand new double-sided business card, rounded cards, embossed logo, nice quality paper
-Include phone (604-382-9145), email (hello@linnearowatt.org), and website (www.linnearowatt.org). No address, please, since I service clients worldwide.
-I'd like the fonts to match those on my website (www.linnearowatt.org). I had to purchase the one font (Born Ready), attached. I'm not sure which version was used on my site so I included all that I purchased. The secondary font is Helvetica
-I'd also like the tagline "Powerful Words. Impressive Results." included.
-My primary brand colour is the teal, colour #19ADC3
Linnea Rowatt | Linnea Rowatt Copywriting & Web Design <hello@linnearowatt.org>
-I'd also like the following services listed on the new cards:
SEO Website Content
SEO Blog Content
SEO Website Design
Contact Information for Business Card
as stated in brief
Font styles to use
Other font styles liked:
- See brief
Look and feel
Each slider illustrates characteristics of the customer's brand and the style your logo design should communicate.

```html
<!DOCTYPE html>
<html lang="en">
<head>
<meta charset="UTF-8">
<title>Linnea Rowatt Copywriting &amp; Web Design – Business Card</title>
<link href="https://fonts.googleapis.com/css2?family=Arimo:wght@400;700&display=swap" rel="stylesheet">
<style>
  :root {
    --page-bg: #e4e6e7;
    --teal-light: #86c3cd;
    --teal-deep: #5aa6b2;
    --brand-teal: #19adc3;
    --rule-teal: #4f9ea9;
    --pattern-teal: rgba(120, 185, 196, 0.28);
    --pattern-white: rgba(255, 255, 255, 0.22);
    --ink: #141414;
    --paper: #ffffff;
  }
  html, body {
    margin: 0;
    padding: 0;
    width: 1200px;
    height: 900px;
    overflow: hidden;
    background: var(--page-bg);
    font-family: "Arimo", "Helvetica Neue", Helvetica, Arial, sans-serif;
  }
  .canvas {
    position: relative;
    width: 1200px;
    height: 900px;
  }
  .card {
    position: absolute;
    left: 270px;
    width: 660px;
    height: 380px;
    border-radius: 26px;
    overflow: hidden;
    box-shadow: 0 6px 18px rgba(0, 0, 0, 0.18);
  }
  .card--front {
    top: 50px;
    background: linear-gradient(135deg, var(--teal-light) 0%, var(--teal-deep) 100%);
  }
  .card--back {
    top: 470px;
    background: var(--paper);
  }
  .pattern {
    position: absolute;
    inset: 0;
  }
  .card--front .pattern {
    background:
      radial-gradient(ellipse 55% 70% at 88% 20%, var(--pattern-white), transparent 70%),
      radial-gradient(ellipse 60% 40% at 15% 100%, var(--pattern-white), transparent 70%);
  }
  .card--back .pattern {
    background:
      radial-gradient(ellipse 50% 75% at 85% 25%, var(--pattern-teal), transparent 70%),
      radial-gradient(ellipse 65% 40% at 30% 100%, var(--pattern-teal), transparent 70%);
  }
  .brand-name {
    position: absolute;
    left: 0;
    right: 0;
    text-align: center;
    margin: 0;
    font-weight: 700;
    font-size: 30px;
    line-height: 1.25;
    letter-spacing: 0.02em;
  }
  .card--front .brand-name {
    top: 135px;
    color: var(--paper);
  }
  .card--back .brand-name {
    top: 75px;
    color: var(--ink);
  }
  .details {
    position: absolute;
    left: 0;
    right: 0;
    top: 232px;
    display: flex;
    justify-content: center;
    align-items: flex-end;
    gap: 16px;
    color: var(--ink);
    font-weight: 700;
    font-size: 17px;
    line-height: 23px;
  }
  .services, .contact {
    list-style: none;
    margin: 0;
    padding: 0;
  }
  .services {
    text-align: right;
    padding-top: 28px;
  }
  .divider {
    width: 2px;
    height: 100px;
    background: var(--rule-teal);
    align-self: stretch;
  }
  .contact {
    align-self: flex-start;
    text-align: left;
  }
</style>
</head>
<body>
<main class="canvas">
  <section class="card card--front" aria-label="Business card front">
    <div class="pattern" role="img" aria-label="Faint palm frond pattern in light teal"></div>
    <h1 class="brand-name">Linnea Rowatt<br>Copywriting &amp; Web Design</h1>
  </section>

  <section class="card card--back" aria-label="Business card back">
    <div class="pattern" role="img" aria-label="Faint palm frond pattern in pale teal"></div>
    <h2 class="brand-name">Linnea Rowatt<br>Copywriting &amp; Web Design</h2>
    <div class="details">
      <ul class="services">
        <li>SEO Website Content</li>
        <li>SEO Blog Content</li>
        <li>SEO Website Design</li>
      </ul>
      <span class="divider"></span>
      <ul class="contact">
        <li>604-382-9145</li>
        <li>hello@linnearowatt.org</li>
        <li>www.linnearowatt.org</li>
      </ul>
    </div>
  </section>
</main>
</body>
</html>
```